Vasel Tea Label & packaging for a premium tea brand. For local and global market

Create a look and feel for a box and rectangle tin. We are looking for a luxe packaging design for a new tea brand based in Kenya called 'Vasel Tea'. Kenya is home to the finest teas in the world and Vasel tea looks to embody that fact. Vasel Tea uses the most premium of Kenyan Tea, Black tea, Purple tea, White Tea, Green tea, Hibiscus Tea and Moringa Tea. Vasel Tea is handpicked from Kenya's highlands. This project will include the look and feel of the different teas described above. The copy on the main face of the box should read 'Premium Kenyan Tea' The box will contain 25 tagged tea bags, with a net weight of 50 gms.

On one side of the box will read 'packaging instructions' To fully savour this Vasel premium tea, use one tea bag for each cup, add some freshly bolded water and wait for 2 minutes as you enjoy the sweet aroma of our tea, stir and serve' Ingredients : Black Tea, and for the others the same : Hibiscus Tea, Green Tea, Purple Tea, White tea. should also feature on the label: Produce of Kenya.

Target Market(s)

Premium

Industry/Entity Type

Agribusiness

Font styles to use
Script

Colors

Designer to choose colors to be used in the design.

Requirements
Must have
• Luxe look and feel
Nice to have
• I have attached the Vasel tea logo and images of brands I'd lile the designer to be inspired by.
Should not have
• Green and yellow colours

```html
<!DOCTYPE html>
<html lang="en">
<head>
<meta charset="utf-8">
<title>Vasel Tea – Black Tea Box Front</title>
<link rel="stylesheet" href="https://fonts.googleapis.com/css2?family=Cinzel:wght@400&display=swap">
<style>
  :root {
    --canvas: #ffffff;
    --panel: #ffffff;
    --panel-edge: #9a9a9a;
    --label-bg: #231f20;
    --label-text: #f2f2f2;
    --brand-gold: #e9ad12;
    --leaf-dark: #1c1f2e;
    --leaf-deep: #2a2236;
    --leaf-mid: #3b3044;
  }
  html, body {
    margin: 0;
    padding: 0;
    width: 1200px;
    height: 1000px;
    overflow: hidden;
    background: var(--canvas);
  }
  .canvas {
    position: relative;
    width: 1200px;
    height: 1000px;
  }
  .box-front {
    position: absolute;
    left: 322px;
    top: 214px;
    width: 556px;
    height: 572px;
    background: var(--panel);
    border: 2px solid var(--panel-edge);
    box-sizing: border-box;
    overflow: hidden;
  }
  .variety-label {
    position: absolute;
    left: 184px;
    top: -2px;
    width: 186px;
    height: 110px;
    background: var(--label-bg);
    color: var(--label-text);
    font-family: "Cinzel", serif;
    text-align: center;
    box-sizing: border-box;
    padding-top: 28px;
  }
  .variety-name {
    display: block;
    font-size: 31px;
    line-height: 32px;
    letter-spacing: 1px;
  }
  .variety-tagline {
    display: block;
    font-size: 11px;
    line-height: 14px;
    letter-spacing: 0.3px;
    margin-top: 1px;
  }
  .brand-name {
    position: absolute;
    left: 0;
    right: 0;
    top: 262px;
    text-align: center;
    font-family: "Cinzel", serif;
    font-weight: 400;
    font-size: 72px;
    line-height: 80px;
    letter-spacing: 4px;
    color: var(--brand-gold);
  }
  .tea-leaf-band {
    position: absolute;
    left: 0;
    right: 0;
    bottom: 0;
    height: 82px;
    background: linear-gradient(90deg, var(--leaf-dark) 0%, var(--leaf-mid) 40%, var(--leaf-deep) 70%, var(--leaf-dark) 100%);
  }
</style>
</head>
<body>
  <main class="canvas">
    <section class="box-front">
      <div class="variety-label">
        <span class="variety-name">Black</span>
        <span class="variety-tagline">Premium Kenyan Tea</span>
      </div>
      <h1 class="brand-name">VASEL</h1>
      <div class="tea-leaf-band" role="img" aria-label="Photograph of loose black tea leaves beside a glass of brewed tea"></div>
    </section>
  </main>
</body>
</html>
```